Colour consulting and Interior design company needs a squarespace web design

we need a website design for squarespace for a Melbourne based company called 'Brightwell Rooms' which incorporates the existing logo. The company primarily provides colour consulting for residential and commercial as well as interior design services. Schemes are personalised for each client. I would like the design to have some colour and use the colour palette provided but it is not is not totally exclusive. The final design should indicate character, playfulness, functionality , harmony and joy. I like the blue/green core colour with the white and would like that to be incorporated.
as per image provided below - double sided
4 page
Requirements
Must have
- space for some images but not too many.
- Page for booking consultation
Should not have
- real images of houses

```html
<!DOCTYPE html>
<html lang="en">
<head>
<meta charset="utf-8">
<title>Brightwell Rooms – Consultation</title>
<link href="https://fonts.googleapis.com/css2?family=Mulish:wght@400;600;700&family=Nunito:wght@700;800;900&display=swap" rel="stylesheet">
<style>
:root{
  --teal:#0e5d78;
  --teal-light:#5f9bae;
  --ink:#111;
  --muted:#333;
  --page:#f4f0f0;
  --field-border:#c9c5c5;
  --white:#fff;
}
*{box-sizing:border-box;margin:0;padding:0}
html,body{width:932px;height:1200px;overflow:hidden}
body{position:relative;font-family:'Mulish',sans-serif;background:var(--page);color:var(--ink)}
.site-header{position:absolute;left:0;top:0;width:932px;height:78px;background:var(--white)}
.brand{position:absolute;left:112px;top:27px;display:flex;align-items:center;gap:8px;font-family:'Mulish',sans-serif;font-weight:700;font-size:22px;color:var(--teal)}
.brand-mark{width:18px;height:18px;background:var(--teal)}
.main-nav{position:absolute;top:36px;left:0;width:932px;font-size:11px;color:var(--ink)}
.main-nav a{position:absolute;color:inherit;text-decoration:none;white-space:nowrap}
.hero{position:absolute;left:0;top:78px;width:932px;height:272px;background:linear-gradient(160deg,#6f7a52 0%,#4a6a3a 35%,#3e5a2c 55%,#5b4a2c 80%,#3a2e1c 100%)}
.hero::after{content:"";position:absolute;inset:0;background:rgba(0,0,0,.28)}
.hero-title{position:absolute;z-index:1;left:0;right:0;top:112px;text-align:center;font-family:'Nunito',sans-serif;font-weight:800;font-size:35px;color:var(--white);letter-spacing:.3px}
.booking{position:absolute;left:112px;top:350px;width:708px}
.booking-title{position:absolute;top:36px;left:0;font-family:'Nunito',sans-serif;font-weight:800;font-size:24px;white-space:nowrap}
.booking-rule{position:absolute;top:71px;left:0;width:706px;height:2px;background:#cfcaca}
.field{position:absolute;height:34px;background:var(--white);border:1px solid var(--field-border);font-size:10.5px;color:var(--muted);padding:0 14px;display:flex;align-items:center}
.field.select .caret{position:absolute;right:14px;top:15px;width:0;height:0;border-left:4px solid transparent;border-right:4px solid transparent;border-top:4px solid #222}
.upload-btn{position:absolute;right:7px;top:7px;height:20px;width:67px;background:var(--teal);color:var(--white);font-weight:700;font-size:9.5px;display:flex;align-items:center;justify-content:center;gap:5px}
.message{position:absolute;left:0;top:250px;width:708px;height:148px;background:var(--white);border:1px solid var(--field-border);font-size:10.5px;color:var(--muted);padding:12px 14px}
.submit{position:absolute;left:2px;top:428px;width:115px;height:41px;background:var(--teal);color:var(--white);font-family:'Nunito',sans-serif;font-weight:800;font-size:15px;display:flex;align-items:center;justify-content:center;letter-spacing:.5px}
.footer-band{position:absolute;left:0;top:876px;width:932px;height:8px;background:var(--teal-light)}
.site-footer{position:absolute;left:0;top:884px;width:932px;height:316px;background:var(--teal);color:var(--white);text-align:center}
.footer-nav{position:absolute;top:42px;left:0;width:100%;font-size:8.8px;letter-spacing:.2px}
.footer-nav span{margin:0 4px}
.footer-brand{position:absolute;top:100px;left:0;width:100%;display:flex;justify-content:center;align-items:center;gap:10px;font-weight:700;font-size:26px}
.footer-brand .brand-mark{width:22px;height:22px;background:var(--white)}
.footer-contact{position:absolute;top:191px;left:0;width:100%;font-size:8.8px}
.footer-rule{position:absolute;top:229px;left:170px;width:652px;height:1px;background:rgba(255,255,255,.18)}
.copyright{position:absolute;top:259px;left:0;width:100%;font-size:8.8px}
</style>
</head>
<body>
<header class="site-header">
  <div class="brand"><span class="brand-mark"></span>Brightwell Rooms</div>
  <nav class="main-nav">
    <a style="left:425px">HOME</a>
    <a style="left:481px">ABOUT US</a>
    <a style="left:557px">SERVICES</a>
    <a style="left:630px">GALLERY</a>
    <a style="left:703px">BLOG</a>
    <a style="left:755px">CONTACT US</a>
  </nav>
</header>

<section class="hero" role="img" aria-label="Photo of a bright living room with green sofas and timber floor">
  <h1 class="hero-title">CONSULTATION</h1>
</section>

<main class="booking">
  <h2 class="booking-title">Book a Consultation</h2>
  <div class="booking-rule"></div>

  <div class="field" style="left:0;top:104px;width:225px">Name</div>
  <div class="field" style="left:243px;top:104px;width:224px">Phone</div>
  <div class="field" style="left:483px;top:104px;width:225px">E mail</div>

  <div class="field" style="left:0;top:150px;width:225px">Address</div>
  <div class="field" style="left:243px;top:150px;width:224px">City</div>
  <div class="field" style="left:483px;top:150px;width:225px">State</div>

  <div class="field" style="left:0;top:200px;width:225px">Which area you are in</div>
  <div class="field select" style="left:243px;top:200px;width:224px">Type of consultation<span class="caret"></span></div>
  <div class="field" style="left:483px;top:200px;width:225px">Attach and upload images
    <span class="upload-btn">
      <svg width="9" height="9" viewBox="0 0 10 10" aria-hidden="true"><path d="M5 0 L9 4 H6.3 V7 H3.7 V4 H1 Z M1 8.2 H9 V10 H1 Z" fill="#fff"/></svg>UPLOAD
    </span>
  </div>

  <div class="message">Message</div>
  <div class="submit">SUBMIT</div>
</main>

<div class="footer-band"></div>
<footer class="site-footer">
  <nav class="footer-nav">HOME<span>|</span> ABOUT US<span>|</span> SERVICES<span>|</span> GALLERY<span>|</span> BLOG<span>|</span> CONTACT US</nav>
  <div class="footer-brand"><span class="brand-mark"></span>Brightwell Rooms</div>
  <p class="footer-contact">48 Larkfield Lane &nbsp;|&nbsp; Fitzroy, VIC 3065 &nbsp;|&nbsp; T : 03.5550.0142</p>
  <div class="footer-rule"></div>
  <p class="copyright">Copyrights @ 2018 All Rights Reserved</p>
</footer>
</body>
</html>
```